PLOVEN Business Card

Coastal Build Additions and Refits. I need a business card designed for this new high end renovation business. I would like the logo centered on the back side with the ABN (37 915 402 176) on the bottom right hand corner.

I would like the following information placed on the other side along with some customized pattern or design.

Derek Collwood
Director
Phone: 1300 480 957
Fax: (02) 8145 9021
Website: www.plovenbuilders.com.au
Email: d.collwood@plovenbuilders.com.au
PO Box 87,
Kelvinbrook NSW 2069

(FB Logo) PLOVEN - Coastal Build Additions and Refits

The final design should communicate professionalism and trust.

Back side background colour: white
Front side: Undecided

```html
<!DOCTYPE html>
<html lang="en">
<head>
<meta charset="utf-8">
<title>PLOVEN Business Card</title>
<link rel="stylesheet" href="https://fonts.googleapis.com/css2?family=Source+Sans+3:wght@400;600;700&display=swap">
<style>
  :root {
    --page-bg: #ecebe8;
    --card-white: #ffffff;
    --card-dark: #333333;
    --brand-blue: #1d4f85;
    --ink: #2b2b2b;
    --ink-light: #f4f4f4;
    --rule: #9a9a9a;
  }
  html, body {
    margin: 0;
    padding: 0;
    width: 1200px;
    height: 957px;
    overflow: hidden;
    background: var(--page-bg);
    font-family: "Source Sans 3", Arial, sans-serif;
  }
  .canvas {
    position: relative;
    width: 1200px;
    height: 957px;
  }
  .card {
    position: absolute;
    width: 581px;
    height: 357px;
    border-radius: 18px;
    overflow: hidden;
    background: var(--card-white);
    box-shadow: 0 6px 14px rgba(0,0,0,0.18);
  }
  .card--front { left: 186px; top: 79px; }
  .card--back  { left: 456px; top: 530px; }

  /* Front */
  .front-top {
    position: relative;
    height: 177px;
  }
  .wordmark {
    font-weight: 700;
    color: var(--brand-blue);
    letter-spacing: 1px;
    line-height: 1;
    margin: 0;
  }
  .front-top .wordmark {
    position: absolute;
    left: 42px;
    top: 70px;
    font-size: 50px;
  }
  .person {
    position: absolute;
    left: 314px;
    top: 80px;
  }
  .person__name {
    margin: 0;
    font-size: 28px;
    font-weight: 400;
    color: var(--brand-blue);
    line-height: 1;
  }
  .person__role {
    margin: 2px 0 0;
    font-size: 20px;
    color: var(--ink);
    line-height: 1;
  }
  .front-bottom {
    position: relative;
    height: 180px;
    background: var(--card-dark);
    color: var(--ink-light);
  }
  .front-bottom__rule {
    position: absolute;
    left: 40px;
    right: 26px;
    top: 55px;
    border-top: 1px solid var(--rule);
  }
  .info-col {
    position: absolute;
    top: 32px;
  }
  .info-col--address { left: 42px; }
  .info-col--contact { left: 314px; }
  .info-col__heading {
    margin: 0;
    font-size: 18px;
    font-weight: 400;
    line-height: 1;
  }
  .address {
    margin: 27px 0 0;
    font-style: normal;
    font-weight: 700;
    font-size: 18px;
    line-height: 25px;
  }
  .web {
    margin: 8px 0 0;
    font-size: 15px;
    font-weight: 600;
  }
  .contact-list {
    list-style: none;
    margin: 25px 0 0;
    padding: 0;
    font-size: 16px;
    line-height: 22px;
  }
  .contact-list b { font-weight: 700; }
  .contact-list .contact-email {
    margin-top: 10px;
    font-size: 14.5px;
  }

  /* Back */
  .back-logo {
    position: absolute;
    left: 0;
    right: 0;
    top: 118px;
    text-align: center;
  }
  .back-logo .wordmark { font-size: 58px; }
  .tagline {
    display: flex;
    align-items: center;
    justify-content: center;
    gap: 8px;
    margin-top: 6px;
    font-size: 16px;
    color: var(--brand-blue);
    letter-spacing: 0.5px;
    text-transform: uppercase;
  }
  .tagline::before, .tagline::after {
    content: "";
    width: 26px;
    border-top: 2px solid var(--brand-blue);
  }
  .abn {
    position: absolute;
    right: 22px;
    bottom: 22px;
    margin: 0;
    font-size: 16px;
    font-weight: 700;
    color: var(--ink);
  }
</style>
</head>
<body>
<main class="canvas">
  <section class="card card--front">
    <div class="front-top">
      <p class="wordmark">PLOVEN</p>
      <div class="person">
        <p class="person__name">Derek Collwood</p>
        <p class="person__role">Director</p>
      </div>
    </div>
    <div class="front-bottom">
      <div class="front-bottom__rule"></div>
      <div class="info-col info-col--address">
        <p class="info-col__heading">Address</p>
        <address class="address">PO Box 87,<br>Kelvinbrook NSW 2069</address>
        <p class="web">www.plovenbuilders.com.au</p>
      </div>
      <div class="info-col info-col--contact">
        <p class="info-col__heading">Contact</p>
        <ul class="contact-list">
          <li><b>P:</b> 1300 480 957</li>
          <li><b>F:</b> (02) 8145 9021</li>
          <li class="contact-email"><b>e:</b> d.collwood@plovenbuilders.com.au</li>
        </ul>
      </div>
    </div>
  </section>

  <section class="card card--back">
    <div class="back-logo">
      <p class="wordmark">PLOVEN</p>
      <p class="tagline">Coastal Build Additions &amp; Refits</p>
    </div>
    <p class="abn">ABN (37 915 402 176)</p>
  </section>
</main>
</body>
</html>
```